Software Development Consulting Company Needs Business Card Design

We need a new business card design for our consultants at Marendo Solutions (marendosolutions.example). We are a small firm that provides high-end software development and methodology consulting to medium to large enterprise IT organizations.

Our logo uses Futura for the font and we would like to stick with navy blue and canary yellow for the logo colors. Attached are normal and reversed versions of our logos in illustrator format.
Updates

Hi Everyone, Thank yo very much for your amazing design ideas. I have created a poll for this project and our employees will be voting on the design they wish to use. We will be making a decision this Wednesday (October 22nd). Thanks again, Gavin Hartwell

Industry/Entity Type

Business

```html
<!DOCTYPE html>
<html lang="en">
<head>
<meta charset="utf-8">
<title>Marendo Solutions – Business Card</title>
<link rel="stylesheet" href="https://fonts.googleapis.com/css2?family=Jost:wght@300;400;500;600&display=swap">
<style>
  :root {
    --navy: #1e3f66;
    --navy-deep: #1a3a60;
    --canary: #f2dd0a;
    --ring: #e4e5e8;
    --white: #ffffff;
    --page: #f1f1f1;
    --label: #151515;
  }
  * { margin: 0; padding: 0; box-sizing: border-box; }
  html, body {
    width: 1200px;
    height: 1196px;
    overflow: hidden;
    background: var(--page);
    font-family: "Jost", "Futura", sans-serif;
  }
  .presentation {
    position: relative;
    width: 1200px;
    height: 1196px;
  }
  .side-label {
    position: absolute;
    top: 27px;
    font-size: 17px;
    font-weight: 600;
    letter-spacing: 0.2px;
    color: var(--label);
  }
  .side-label--front { left: 70px; }
  .side-label--back { left: 619px; }
  .card {
    position: absolute;
    top: 68px;
    width: 505px;
    height: 280px;
  }
  .card--front { left: 70px; }
  .card--back { left: 620px; }
  .card svg { display: block; width: 505px; height: 280px; }
  .brand-name { font-family: "Jost", "Futura", sans-serif; font-weight: 400; letter-spacing: 2.2px; }
  .web-address { font-family: "Jost", "Futura", sans-serif; font-size: 11.5px; font-weight: 400; fill: var(--white); }
  .holder-name { font-family: "Jost", "Futura", sans-serif; font-size: 24px; font-weight: 600; fill: var(--white); letter-spacing: -0.3px; }
  .holder-title { font-family: "Jost", "Futura", sans-serif; font-size: 18px; font-weight: 300; fill: var(--white); }
  .office { font-family: "Jost", "Futura", sans-serif; font-size: 12px; font-weight: 300; fill: var(--white); }
</style>
</head>
<body>
<main class="presentation">
  <h2 class="side-label side-label--front">SIDE A</h2>
  <h2 class="side-label side-label--back">SIDE B</h2>

  <section class="card card--front" aria-label="Business card front">
    <svg viewBox="0 0 505 280">
      <defs>
        <clipPath id="front-clip"><rect width="505" height="280" rx="12"/></clipPath>
      </defs>
      <g clip-path="url(#front-clip)">
        <rect class="card-base" width="505" height="280" fill="var(--canary)"/>
        <circle class="outer-ring" cx="252" cy="137" r="218" fill="var(--ring)"/>
        <circle class="inner-disc" cx="252" cy="137" r="185" fill="var(--navy)"/>
        <circle class="brand-dot" cx="150" cy="141" r="5" fill="var(--canary)"/>
        <text class="brand-name" x="262" y="146" text-anchor="middle" font-size="16" fill="var(--white)">MARENDO SOLUTIONS</text>
        <text class="web-address" x="252" y="262" text-anchor="middle">www.marendosolutions.example</text>
      </g>
    </svg>
  </section>

  <section class="card card--back" aria-label="Business card back">
    <svg viewBox="0 0 505 280">
      <defs>
        <clipPath id="back-clip"><rect width="505" height="280" rx="12"/></clipPath>
      </defs>
      <g clip-path="url(#back-clip)">
        <rect class="card-base" width="505" height="280" fill="var(--white)"/>
        <circle class="accent-edge" cx="500" cy="294" r="290" fill="var(--canary)"/>
        <circle class="info-panel" cx="505" cy="292" r="287" fill="var(--navy-deep)" role="img" aria-label="Soft navy technology backdrop behind contact details"/>
        <circle class="brand-dot" cx="40" cy="67" r="5" fill="var(--canary)"/>
        <text class="brand-name" x="52" y="73" font-size="16" fill="var(--navy)">MARENDO SOLUTIONS</text>

        <text class="holder-name" x="470" y="128" text-anchor="end">DANIEL REYES</text>
        <text class="holder-title" x="470" y="152" text-anchor="end">President</text>
        <rect class="divider" x="337" y="166" width="131" height="2" fill="var(--canary)"/>
        <text class="office" x="470" y="193" text-anchor="end">Harlow, IL</text>
        <text class="office" x="470" y="211" text-anchor="end">Brantleyville, IL</text>
        <text class="office" x="470" y="229" text-anchor="end">Fenwick, MO</text>
        <text class="office" x="470" y="247" text-anchor="end">Corliss, CO</text>

        <circle class="social-badge" cx="37" cy="248" r="10" fill="var(--navy)"/>
        <circle class="social-badge" cx="64" cy="248" r="10" fill="var(--navy)"/>
      </g>
    </svg>
  </section>
</main>
</body>
</html>
```